Brightwave Audiology Letterhead redesign project

We need a full redesign of our current letterhead to make it consistent with the look and feel of our website design www.brightwaveaudio.com.au. It will need to include all information on the current version attached. The letterhead is used for sending medical reports and general correspondence. It should make use of our corporate colours (purple and teal) as per the logo on the existing file. The letterhead should be bold and eye-catching.

Target Market(s)

Medical practitioners.

Font styles to use
Sans Serif

Requirements
Must have
• It will need to include all information on the current version. Must have a premium, professional, high-end look and feel.
Nice to have
• Bold and eye-catching letterhead that reinforces the Brightwave Audiology brand. To stand out from other traditional letterheads.
Should not have
• The design should not be too cluttered or 'busy'

```html
<!DOCTYPE html>
<html lang="en">
<head>
<meta charset="utf-8">
<title>Brightwave Audiology Letterhead</title>
<link href="https://fonts.googleapis.com/css2?family=Roboto:wght@400;700&display=swap" rel="stylesheet">
<style>
  :root {
    --purple: #6b2a8c;
    --teal: #13b28d;
    --paper: #fbfbfb;
    --ink: #7a7a7a;
    --backdrop: #e4e4e4;
  }
  * { box-sizing: border-box; margin: 0; padding: 0; }
  html, body { width: 1200px; height: 866px; overflow: hidden; }
  body {
    background: var(--backdrop);
    font-family: "Roboto", Arial, sans-serif;
    position: relative;
  }
  .letterhead {
    position: absolute;
    left: 307px; top: 23px;
    width: 585px; height: 820px;
    background: var(--paper);
    overflow: hidden;
  }
  .brand {
    position: absolute;
    left: 50px; top: 46px;
    color: var(--purple);
    font-weight: 700;
    font-size: 25px;
    line-height: 27px;
    letter-spacing: -0.5px;
  }
  .bubble { position: absolute; left: 0; top: 0; }
  .contact {
    position: absolute;
    left: 412px; top: 46px;
    color: #fff;
    font-style: normal;
    font-size: 9.5px;
    line-height: 13.5px;
  }
  .contact .address { margin-bottom: 3px; }
  .contact li { list-style: none; display: flex; align-items: center; gap: 4px; }
  .contact svg { width: 8px; height: 8px; fill: var(--purple); flex: none; }
  .recipient {
    position: absolute;
    left: 50px; top: 247px;
    color: var(--ink);
    font-size: 10.5px;
    line-height: 15.2px;
  }
  .letter-body {
    position: absolute;
    left: 50px; top: 338px;
    width: 486px;
    color: var(--ink);
    font-size: 10.2px;
    line-height: 15.2px;
    text-align: justify;
  }
  .letter-body p + p { margin-top: 30px; }
  .signature {
    position: absolute;
    left: 50px; top: 556px;
    width: 110px; height: 72px;
    background: linear-gradient(120deg, rgba(107,42,140,0.18), rgba(107,42,140,0.06));
    border-radius: 4px;
  }
  .signatory {
    position: absolute;
    left: 50px; top: 643px;
    color: var(--ink);
    font-size: 10.5px;
  }
  .footer-band { position: absolute; bottom: 0; height: 12px; }
  .footer-band.purple { left: 0; width: 361px; background: var(--purple); }
  .footer-band.teal { left: 365px; right: 0; background: var(--teal); }
</style>
</head>
<body>
  <main class="letterhead">
    <svg class="bubble" width="585" height="270" viewBox="0 0 585 270" aria-hidden="true">
      <ellipse cx="500" cy="70" rx="152" ry="122" fill="var(--teal)"/>
      <polygon points="438,160 443,257 530,175" fill="var(--teal)"/>
    </svg>

    <header class="brand">Brightwave<br>Audiology</header>

    <address class="contact">
      <div class="address">48 Marlow Street, Eastvale<br>NSW 2790</div>
      <ul>
        <li><svg viewBox="0 0 10 10"><path d="M2 0.5 L4 2.5 L3 4 Q4 6 6 7 L7.5 6 L9.5 8 L8 9.5 Q3 9 0.5 2 Z"/></svg>02 6300 2815</li>
        <li><svg viewBox="0 0 10 10"><rect x="2.5" y="0.5" width="5" height="3"/><rect x="0.5" y="3.5" width="9" height="4" rx="1"/><rect x="2.5" y="7" width="5" height="2.5"/></svg>02 6300 2816</li>
        <li><svg viewBox="0 0 10 10"><path d="M0.5 2 H9.5 V8.5 H0.5 Z"/></svg>hello@brightwaveaudio.com.au</li>
        <li><svg viewBox="0 0 10 10"><circle cx="5" cy="5" r="4.5"/></svg>www.brightwaveaudio.com.au</li>
      </ul>
    </address>

    <section class="recipient">
      Dear Halvorsen<br>
      Corvell Design Group<br>
      Department Design
    </section>

    <section class="letter-body">
      <p>Lorem ipsum dolor sit amet, consectetuer adipiscing elit. Aenean commodo ligula eget dolor. Aenean massa. Cum sociis natoque penatibus et magnis dis parturient montes, nascetur ridiculus mus. Donec quam felis, ultricies nec, pellentesque eu, pretium quis, sem. Nulla consequat massa quis enim. Donec pede justo, fringilla vel, aliquet nec, vulputate eget, arcu. In enim justo, rhoncus ut, imperdiet a, venenatis vitae, justo. Nullam dictum felis eu pede mollis pretium. Integer tincidunt. Cras dapibus. Vivamus elementum semper nisi.Nullam dictum felis eu pede mollis pretium. Integer tincidunt. Cras dapibus. Vivamus elementum semper nisi.felis eu pede mollis pretium. Integer tincidunt. Cras dapibus.</p>
      <p>Quisque rutrum. Aenean imperdiet. Etiam ultricies nisi vel augue. Curabitur ullamcorper ultricies nisi. Nam eget dui. Etiam rhoncus. Maecenas tempus, tellus eget condimentum rhoncus, sem quam semper libero, sit amet adipiscing sem neque sed ipsum.felis pede mollis pretium. I am tincidunt. Cras dapibus.</p>
    </section>

    <div class="signature" role="img" aria-label="Handwritten signature of the director"></div>
    <div class="signatory">Director/Excecutive Director</div>

    <div class="footer-band purple"></div>
    <div class="footer-band teal"></div>
  </main>
</body>
</html>
```